Publisher needs a book cover design for Enterprise Flow Study book

We need a book cover (front, back, spine) for the 3rd edition of a book entitled 'Enterprise Flow Study' and subtitled 'covering Design, Governance, Control and Growth'. The author is Marcus Thelwell. The publisher is Kestrelmoor Press. The finished size of the paperback version will be the industry standard 9" x 6". There will be paperback, hardback, and Kindle versions. The final number of pages is expected to be in the region 300-350 pages. Text for the back cover is not yet available, but at the bottom of the back cover should be publisher logo on the left and space for the ISBN bar code on the right.<br/>The design should be original and not include any stock images that have been created by someone else or may require obtaining a copyright licence to use. Symbols in common use and not copyrighted are probably ok.<br/>There are no required images, photographs or symbols except the publisher logo at the left bottom of the back cover and lower spine. S[ine lettering should be UK/US style with the top of the writing nearest the front cover. The designer is free to be creative using appropriate diagrams, symbols or abstract designs. Rectangular and circular variants of the publisher logo are attached.<br/>I just want to assure designers that when evaluating designs from my perspective, I take absolutely no notice whatsoever of a designer's Pixel Forum ranking or status; I am completely output driven, so what matters to me is the design, not the ranking or status of the designer. In a similar way, I do not evaluate designs as 'good' or 'bad' - the winning design will be chosen after review by a design panel.
Updates

More time is needed to check the use of stock images by designers. Some have been used by desitgners but not yet disclosed.

Target Market(s)

Practitioners and academics concerned with Enterprise Flow Study, Business Process Management, Business Process Architecture, Enterprise Architecture, Information Architecture, Process modelling, data modelling

Font styles to use
Serif
Sans Serif

Colors

Designer to choose colors to be used in the design.

Requirements
Must have
• Title, author, edition, subtitle, publisher logo.
Nice to have
• Originality, innovation
Should not have
• Stock images or anything else requiring additional copyright discussions and negotiations.

```html
<!DOCTYPE html>
<html lang="en">
<head>
<meta charset="utf-8">
<title>Enterprise Flow Study – Cover Spread</title>
<link rel="stylesheet" href="https://fonts.googleapis.com/css2?family=Bebas+Neue&family=EB+Garamond:wght@400;500&family=Oswald:wght@200;300&display=swap">
<style>
  :root {
    --paper: #ffffff;
    --ink: #33475b;
    --crimson: #d4003f;
    --plum: #8a2257;
    --mauve: #633c62;
    --body-text: #2f3a47;
  }
  * { margin: 0; padding: 0; box-sizing: border-box; }
  html, body {
    width: 1200px;
    height: 830px;
    overflow: hidden;
    background: var(--paper);
  }
  .spread {
    position: relative;
    width: 1200px;
    height: 830px;
    background: var(--paper);
  }
  .back-copy {
    position: absolute;
    left: 56px;
    top: 74px;
    width: 440px;
    font-family: "EB Garamond", Georgia, serif;
    font-size: 13.6px;
    line-height: 17px;
    color: var(--body-text);
    text-align: justify;
    hyphens: auto;
  }
  .back-copy p + p { margin-top: 17px; }
  .cover-art {
    position: absolute;
    inset: 0;
  }
  .display { font-family: "Bebas Neue", "Oswald", sans-serif; }
  .thin { font-family: "Oswald", sans-serif; font-weight: 200; }
  .light { font-family: "Oswald", sans-serif; font-weight: 300; }
  .imprint { font-family: "EB Garamond", Georgia, serif; font-weight: 500; }
</style>
</head>
<body>
<main class="spread">

  <section class="back-copy" aria-label="Back cover blurb">
    <p>Lorem ipsum dolor sit amet, consectetur adipiscing elit. Suspendisse eget tellus sapien. Nulla tempus, nisl id posuere porta, odio leo ultricies massa, a fermentum lacus eros vitae turpis. Pellentesque a tristique est. Integer rhoncus molestie tellus ut iaculis. Sed nibh dolor, vehicula at bibendum vel, mollis sed dui. Orci varius natoque penatibus et magnis dis parturient montes, nascetur ridiculus mus. Nullam sollicitudin facilisis tortor. In vitae magna nec leo luctus fermentum.</p>
    <p>Mauris iaculis eget lacus sed lobortis. Vestibulum aliquet consectetur finibus. Duis vestibulum quam nec facilisis aliquam. Integer interdum dui vel velit laoreet, eget molestie lorem commodo. Suspendisse ac enim sit amet erat mollis maximus nec sit amet lacus. Nulla facilisi. Nulla facilisis molestie ex. Aliquam aliquam massa elit, ut fringilla ipsum faucibus a. Phasellus non nisi dignissim, fermentum dui in, porttitor elit. In lorem lorem, tincidunt nec suscipit nec, interdum ut nibh. Duis non ultrices tellus. Donec non pulvinar nulla, non bibendum lacus.</p>
  </section>

  <svg class="cover-art" width="1200" height="830" viewBox="0 0 1200 830" xmlns="http://www.w3.org/2000/svg">
    <defs>
      <linearGradient id="quilt-tones" x1="0" y1="0" x2="1" y2="1">
        <stop offset="0" stop-color="#633c62"/>
        <stop offset="0.3" stop-color="#8a2257"/>
        <stop offset="0.5" stop-color="#33475b"/>
        <stop offset="0.7" stop-color="#8a2257"/>
        <stop offset="1" stop-color="#d4003f"/>
      </linearGradient>
    </defs>

    <!-- Back cover imprint -->
    <g class="back-imprint">
      <circle cx="91" cy="734" r="34" fill="var(--ink)"/>
      <text class="imprint" x="136" y="744" font-size="27" letter-spacing="1.5" fill="var(--ink)">KESTRELMOOR PRESS</text>
    </g>

    <!-- Spine -->
    <g class="spine">
      <text class="display" transform="translate(584 32) rotate(90)" font-size="46" fill="var(--ink)" textLength="400" lengthAdjust="spacingAndGlyphs">ENTERPRISE FLOW STUDY</text>
      <text class="thin" transform="translate(586 466) rotate(90)" font-size="37" fill="var(--ink)" textLength="218" lengthAdjust="spacingAndGlyphs">MARCUS THELWELL</text>
      <text class="display" transform="translate(591 704) rotate(90)" font-size="17" fill="var(--crimson)">3<tspan font-size="10" dy="-5">RD</tspan><tspan dy="5"> EDITION</tspan></text>
      <circle cx="598" cy="790" r="18" fill="var(--ink)"/>
    </g>

    <!-- Front cover -->
    <g class="front">
      <text class="display" x="706" y="164" font-size="180" fill="var(--ink)" textLength="432" lengthAdjust="spacingAndGlyphs">ENTERPRISE</text>
      <text class="display" x="708" y="208" font-size="74" fill="var(--ink)" textLength="428" lengthAdjust="spacing">FLOW STUDY</text>
      <text class="light" x="708" y="248" font-size="18" fill="var(--crimson)" textLength="428" lengthAdjust="spacingAndGlyphs">COVERING DESIGN, GOVERNANCE, CONTROL AND GROWTH</text>

      <rect x="706" y="274" width="422" height="416" fill="url(#quilt-tones)" role="img" aria-label="Geometric quilt-star artwork of triangles in slate, crimson, plum and teal"/>

      <text class="thin" x="704" y="764" font-size="80" fill="var(--ink)" textLength="428" lengthAdjust="spacingAndGlyphs">MARCUS THELWELL</text>
      <text class="display" x="918" y="806" font-size="31" fill="var(--crimson)" text-anchor="middle">3<tspan font-size="17" dy="-11">RD</tspan><tspan dy="11"> EDITION</tspan></text>
    </g>
  </svg>

</main>
</body>
</html>
```